Design a menu for health restaurant

A health food restaurant in Los Angeles is seeking menu design. Our foods are made from scratch using whole ingredients.
Name: Grubb Larder
Address: 1000 E 60th StLos Angeles, CA 90247
Website: www.GrubbLarder.example
We are looking for a clean and simple menu. Brand colors are white/tan, green and orange.

Please see attached excel with menu items and logo. We do not yet have prices.

Colors
f78f20
9bcb3c
ffffff
fff3d1

Requirements
Must have
• Easy to read.
Trifold menu design (front and back).
VEGAN, VEGETARIAN, GLUTEN FREE, CONTAINS NUTS symbols.
Logo.
Nice to have
• Incorporate brand colors, but still be easy to read.
We would like to use the Belco font (attached) if it works. If not we are open to a similar font that is easy to read.

Please see attached images.
We like the images and headers of OPTION 1. Would like something similar in trifold format.
We like the clean fonts of OPTION 2.

```html
<!DOCTYPE html>
<html lang="en">
<head>
<meta charset="utf-8">
<title>Grubb Larder – Menu</title>
<link rel="stylesheet" href="https://fonts.googleapis.com/css2?family=Sansita:ital,wght@1,800&family=Baloo+2:wght@800&family=Source+Sans+3:wght@300;400&display=swap">
<style>
:root{
  --orange:#f78f20;
  --green:#9bcb3c;
  --cream:#fff3d1;
  --white:#ffffff;
  --ink:#111111;
  --pink:#f08a9b;
  --peach:#fbcdb8;
}
*{margin:0;padding:0;box-sizing:border-box}
html,body{width:1200px;height:925px;overflow:hidden;background:var(--white)}
.menu{position:relative;width:1200px;height:925px;color:var(--ink);font-family:"Source Sans 3",Arial,sans-serif;font-weight:300}
.frames{position:absolute;left:0;top:0}
.section-title{position:absolute;height:27px;background:var(--cream);border:2.5px solid var(--orange);border-radius:14px;
  font-family:"Sansita",Georgia,serif;font-style:italic;font-weight:800;font-size:21px;line-height:22px;text-align:center;letter-spacing:.4px;z-index:2;white-space:nowrap}
.block{position:absolute;font-size:16px;line-height:18.2px}
.block p{white-space:nowrap}
.spaced .item{margin-bottom:4.4px}
.item-name{position:relative;font-family:"Baloo 2",Arial,sans-serif;font-weight:800;font-size:14.6px;line-height:18.2px;height:18.2px;white-space:nowrap}
.tags{position:absolute;top:3px;display:inline-flex;gap:4px}
.line{position:relative}
.tag{display:inline-flex;align-items:center;justify-content:center;width:12px;height:12px;border:1px solid #444;font:400 6.5px/1 Arial,sans-serif;color:#333;background:transparent}
.tag-gf{border-radius:50%}
.tag-nut{border-radius:4px}
.small{font-size:10px}
.desserts-box{position:absolute;left:398px;top:672px;width:337px;height:235px;background:var(--peach);border-radius:14px}
.logo-mark{position:absolute;left:907px;top:49px;width:156px;height:156px;border-radius:50%;background:var(--orange)}
.brand-name{position:absolute;left:850px;top:206px;width:275px;text-align:center;color:var(--orange);font-family:"Source Sans 3",Arial,sans-serif;font-weight:300;font-size:78px;line-height:62px}
.photo{position:absolute;left:800px;top:378px}
.contact{position:absolute;left:815px;top:822px;width:345px;text-align:center;color:var(--green);font-size:18px;line-height:29px;font-weight:300;font-style:normal}
</style>
</head>
<body>
<main class="menu">

<svg class="frames" width="1200" height="925" viewBox="0 0 1200 925" aria-hidden="true">
  <path d="M134 46 L338 46 L349 69 L349 465 L338 483 L36 483 L32 465 L32 69" fill="none" stroke="var(--green)" stroke-width="5" stroke-linecap="round" stroke-dasharray="0 20.5"/>
  <path d="M531 49 L705 49 L734 58 L734 603 L705 633 L435 633 L400 607 L400 65" fill="none" stroke="var(--orange)" stroke-width="9" stroke-linecap="round" stroke-dasharray="0 21.8"/>
  <path d="M178 734 L335 734 L342 750 L342 895 L335 907 L44 907 L36 895 L36 756" fill="none" stroke="var(--pink)" stroke-width="4.5" stroke-linecap="round" stroke-dasharray="0 10.5"/>
</svg>

<!-- Salad -->
<h2 class="section-title" style="left:32px;top:33px;width:81px">Salad</h2>
<section class="block" style="left:43px;top:59px">
  <div class="item"><div class="item-name">Avocado, Golden Beet, and Cranberry Salad</div>
    <p class="line">Gold beets, avocado, dried cranberries, <span class="tags" style="left:266px"><span class="tag">V</span><span class="tag tag-gf">GF</span></span></p>
    <p>watermelon radish, red kale, romaine, mixed<br>greens, and pepitas served with Golden<br>Buddha dressing.</p></div>
  <div class="item"><div class="item-name">Burrata Salad <span class="tags" style="left:132px"><span class="tag">V</span><span class="tag tag-gf">GF</span></span></div>
    <p>Tomato, melon, shredded basil, balsamic<br>glaze, fresh cracked pepper, and olive oil with<br>burrata.</p></div>
  <div class="item"><div class="item-name">Mediterranean Salad <span class="tags" style="left:173px"><span class="tag">V</span><span class="tag tag-gf">GF</span></span></div>
    <p>Cucumbers, Kalamata olives, cherry tomatoes,<br>parsley, tricolor quinoa, hard-boiled egg, and<br>hummus on mixed greens, romaine, and red<br>cabbage with lemon-olive oil dressing.</p></div>
  <div class="item"><div class="item-name">Vegan Chef Salad <span class="tags" style="left:173px"><span class="tag">V</span><span class="tag tag-gf">GF</span><span class="tag tag-nut">N+</span></span></div>
    <p>Roasted potatoes and carrots, chickpeas,<br>avocado, microgreens and walnuts on mixed<br>greens, romaine, and red kale with vegan<br>ranch.</p></div>
  <div class="item"><div class="item-name">Rancher’s Salad <span class="tags" style="left:173px"><span class="tag">V</span><span class="tag tag-gf">GF</span></span></div>
    <p>Tomato, red onion, hard boiled egg, avocado,<br>feta cheese, microgreens, and grilled chicken<br>on romaine with Ranch dressing.</p></div>
</section>

<!-- Snacks -->
<h2 class="section-title" style="left:31px;top:492px;width:191px">Snacks N’ Sides</h2>
<section class="block spaced" style="left:43px;top:518px">
  <div class="item"><div class="item-name">Fries <span class="tags" style="left:60px"><span class="tag">V+</span><span class="tag tag-gf">GF</span></span></div>
    <p>Hand cut air-fries with house seasonings.<br>Choose regular or sweet potato fries.</p></div>
  <div class="item"><div class="item-name">Side Salad</div>
    <p>Your choice of House, Golden Beet,<br>Mediterranean, or Vegan Chef side salad. <span class="small">(24oz)</span></p></div>
  <div class="item"><div class="item-name">Guac + Chips <span class="tags" style="left:108px"><span class="tag">V+</span><span class="tag tag-gf">GF</span></span></div>
    <p>Guacamole with blue corn tortilla chips.</p></div>
  <div class="item"><div class="item-name">Hummus + Chips <span class="tags" style="left:134px"><span class="tag">V+</span><span class="tag tag-gf">GF</span></span></div>
    <p>Hummus with blue corn tortilla chips.</p></div>
</section>

<!-- Smoothies -->
<h2 class="section-title" style="left:31px;top:721px;width:136px">Smoothies</h2>
<section class="block spaced" style="left:43px;top:746px">
  <div class="item"><div class="item-name">Green Machine Smoothie <span class="tags" style="left:190px"><span class="tag">V+</span><span class="tag tag-gf">GF</span><span class="tag tag-nut">N+</span></span></div>
    <p>Romaine, spinach, banana, mango,<br>pineapple, flaxmilk, spirulina, almond butter</p></div>
  <div class="item"><div class="item-name">Acai Smoothie <span class="tags" style="left:123px"><span class="tag">V+</span><span class="tag tag-gf">GF</span><span class="tag tag-nut">N+</span></span></div>
    <p>Acai, blueberries, banana, pineapple, Macqui<br>berry, flaxmilk, almond butter</p></div>
  <div class="item"><div class="item-name">Mango Smoothie <span class="tags" style="left:136px"><span class="tag">V+</span><span class="tag tag-gf">GF</span></span></div>
    <p>Mango, flaxmilk, banan, hemp seeds</p></div>
</section>

<!-- Drinks -->
<h2 class="section-title" style="left:411px;top:36px;width:102px">Drinks</h2>
<section class="block spaced" style="left:418px;top:63px">
  <div class="item"><div class="item-name">Coffee</div>
    <p>We proudly serve Ridgeline Coffee, a local<br>roaster.</p></div>
  <div class="item"><div class="item-name">Power Date Shake <span class="tags" style="left:156px"><span class="tag">V+</span><span class="tag tag-gf">GF</span></span></div>
    <p>Ice-blended energy smoothie featuring dates<br>and coffee.</p></div>
  <div class="item"><div class="item-name">Heart Beet Juice <span class="tags" style="left:156px"><span class="tag">V+</span><span class="tag tag-gf">GF</span></span></div>
    <p>Red beet, apple, carrot, ginger, parsley, and<br>lemon.</p></div>
  <div class="item"><div class="item-name">Green Leafy Juice <span class="tags" style="left:156px"><span class="tag">V+</span><span class="tag tag-gf">GF</span></span></div>
    <p>Spinach, kale, cucumber, apple, and oranges.</p></div>
  <div class="item"><div class="item-name">Orange Turmeric Juice <span class="tags" style="left:182px"><span class="tag">V+</span><span class="tag tag-gf">GF</span></span></div>
    <p>Turmeric, ginger, lemon, carrot, and orange<br>topped with cracked black pepper.</p></div>
  <div class="item"><div class="item-name">Fireshot</div>
    <p>Ginger and lemon shot topped with cayenne.</p></div>
  <div class="item"><div class="item-name">Lemonade</div>
    <p>House Made Lemonade. Choice of<br>unsweetened or agave sweetened in Regular,<br>Raspberry, and Lavender flavors.</p></div>
  <div class="item"><div class="item-name">Tea</div>
    <p>Hot or iced.</p></div>
  <div class="item"><div class="item-name">Bottled Drinks</div>
    <p>“Fernwell kombucha (Blend Trilogy, Blend<br>Gingerberry, Blend Mango)<br>Brightfizz (Orange Mango, Lemon, Grapefruit)<br>Palmera Coco Original<br>Sparkling Water (Evergreen)<br>Still Water (Evergreen)”</p></div>
</section>

<!-- Desserts -->
<div class="desserts-box"></div>
<h2 class="section-title" style="left:406px;top:654px;width:114px">Desserts</h2>
<section class="block" style="left:418px;top:679px">
  <div class="item" style="margin-bottom:4.4px"><div class="item-name">Date Coffee Cake <span class="tags" style="left:148px"><span class="tag">V+</span><span class="tag tag-nut">N+</span></span></div>
    <p>Signature date coffee cake with walnuts.</p></div>
  <div class="item" style="margin-bottom:4.4px"><div class="item-name">Fruit + Spices <span class="tags" style="left:122px"><span class="tag">V+</span><span class="tag tag-gf">GF</span></span></div>
    <p>Strawberry, pineapple, green apple, orange,<br>and blueberries with lime and chili seasoning.</p></div>
  <div class="item" style="margin-bottom:5.5px"><div class="item-name">Cookies <span class="tags" style="left:80px"><span class="tag">V</span></span></div>
    <p>Your choice of Chocolate Chip or Double<br>Chocolate Chip fresh baked cookie.</p></div>
  <div class="item"><div class="item-name">Larder Chocolate Mousse <span class="tags" style="left:210px"><span class="tag">V+</span><span class="tag tag-gf">GF</span></span></div>
    <p>Served with grated dark chocolate.</p></div>
</section>

<!-- Cover panel -->
<div class="logo-mark" aria-hidden="true"></div>
<h1 class="brand-name">Grubb<br>Larder</h1>

<svg class="photo" width="400" height="444" viewBox="0 0 400 444" role="img" aria-label="Photo of a fresh green salad with shredded carrots, beets and cherry tomatoes">
  <defs>
    <linearGradient id="salad-tone" x1="0" y1="0" x2="1" y2="1">
      <stop offset="0" stop-color="#c9d9a0"/>
      <stop offset=".45" stop-color="#6e9a3c"/>
      <stop offset="1" stop-color="#d9823a"/>
    </linearGradient>
  </defs>
  <path d="M70 55 C150 5 270 -5 330 35 C380 75 400 170 398 250 C395 320 360 390 320 444 C250 420 130 440 50 420 C10 360 0 260 15 180 C25 120 35 85 70 55 Z" fill="url(#salad-tone)"/>
</svg>

<address class="contact">
  2417 W 83rd StLos Angeles, CA 90247<br>
  www.GrubbLarder.example
</address>

</main>
</body>
</html>
```